Consulting company requires a logo and business card design

I require a logo/business card design for a new company based in Sexsmith Alberta called TanRidge Field Advisory Ltd. I plan to provide the following services: Construction management/inspection for the oil and gas industry, as well as general consulting for Asset Management, fleet management, etc. Have attached a copy of resume for use as guide for

Target Market(s)

Businesses within the oil and gas production, construction and shipping industry

Industry/Entity Type

Oil And Gas

Contact Information for Business Card

Believe should highlight, services offered, safety, quality,

Logo Text

TanRidge Field Advisory (TRFA) ?

Font styles to use
Script

Requirements
Must have
• Open to all options

```html
<!DOCTYPE html>
<html lang="en">
<head>
<meta charset="utf-8">
<title>TanRidge Field Advisory Ltd. – Business Cards</title>
<link rel="stylesheet" href="https://fonts.googleapis.com/css2?family=Open+Sans:wght@400;600;700&display=swap">
<style>
  :root {
    --backdrop: #e9e6e1;
    --card-dark: #2a2a2b;
    --card-dark-line: #323233;
    --card-light: #ffffff;
    --ink: #2b2b2b;
    --ink-soft: #3c3c3c;
    --accent-red: #d8401f;
    --accent-orange: #ee7a22;
    --accent-blue: #4f86d6;
    --accent-sky: #7fd0f0;
    --logo-blue: #5aa7e6;
    --on-dark: #f4f4f4;
  }
  * { box-sizing: border-box; margin: 0; padding: 0; }
  html, body { width: 1200px; height: 900px; overflow: hidden; }
  body {
    background: var(--backdrop);
    font-family: "Open Sans", Arial, sans-serif;
    position: relative;
  }
  .card {
    position: absolute;
    width: 580px;
    height: 330px;
    border-radius: 3px;
    box-shadow: 0 10px 24px rgba(0,0,0,0.18);
    overflow: hidden;
  }
  /* Back of card */
  .card--back {
    left: 560px; top: 90px;
    background: repeating-linear-gradient(90deg, var(--card-dark) 0 3px, var(--card-dark-line) 3px 5px);
    color: var(--on-dark);
    text-align: center;
  }
  .wordmark {
    display: flex;
    align-items: center;
    justify-content: center;
    gap: 18px;
  }
  .wordmark__dot {
    width: 46px; height: 46px;
    border-radius: 50%;
    flex: none;
  }
  .wordmark__text { text-align: left; font-weight: 400; line-height: 1; }
  .wordmark__name { display: block; font-size: 50px; letter-spacing: 1px; }
  .wordmark__sub { display: block; font-size: 17px; letter-spacing: 5px; margin-top: 8px; }
  .card--back .wordmark { margin-top: 70px; }
  .card--back .wordmark__dot { background: var(--on-dark); }
  .card--back .wordmark__text { color: var(--on-dark); }
  .tagline {
    margin: 34px auto 0;
    width: 470px;
    font-size: 14px;
    line-height: 1.4;
  }
  /* Front of card */
  .card--front {
    left: 70px; top: 480px;
    background: var(--card-light);
    color: var(--ink);
  }
  .corner-tab { position: absolute; left: 0; top: 0; }
  .person { position: absolute; left: 60px; top: 18px; }
  .person__name { font-size: 19px; font-weight: 700; color: var(--accent-red); line-height: 1.2; }
  .person__role { font-size: 13px; color: var(--ink-soft); }
  .contact {
    position: absolute; left: 26px; top: 118px;
    font-size: 14px; line-height: 1.35; color: var(--ink);
  }
  .contact__address { margin-bottom: 12px; }
  .contact__line { display: flex; align-items: center; gap: 8px; }
  .contact__icon { width: 12px; height: 12px; fill: var(--accent-red); flex: none; }
  .card--front .wordmark { position: absolute; left: 250px; top: 140px; gap: 14px; }
  .card--front .wordmark__dot { width: 40px; height: 40px; background: var(--logo-blue); }
  .card--front .wordmark__text { color: var(--logo-blue); }
  .card--front .wordmark__name { font-size: 40px; }
  .card--front .wordmark__sub { font-size: 14px; letter-spacing: 4px; }
  .bottom-bands { position: absolute; left: 0; bottom: 0; }
</style>
</head>
<body>

  <section class="card card--back" aria-label="Card back">
    <div class="wordmark">
      <span class="wordmark__dot"></span>
      <p class="wordmark__text">
        <span class="wordmark__name">TanRidge</span>
        <span class="wordmark__sub">Field Advisory Ltd.</span>
      </p>
    </div>
    <p class="tagline">We are a construction management/inspection for the oil and gas industry, as well as general consulting for Asset Management, fleet management.</p>
  </section>

  <section class="card card--front" aria-label="Card front">
    <svg class="corner-tab" width="54" height="46" viewBox="0 0 54 46">
      <polygon points="0,0 18,0 0,30" fill="var(--accent-orange)"/>
      <polygon points="24,0 54,0 54,46 8,46" fill="var(--accent-blue)"/>
    </svg>
    <div class="person">
      <p class="person__name">Dana Mercer</p>
      <p class="person__role">Managing Director</p>
    </div>
    <div class="contact">
      <p class="contact__address">410 Railway Avenue,<br>Sexsmith, AB T0H 3C0</p>
      <p class="contact__line">
        <svg class="contact__icon" viewBox="0 0 12 12"><path d="M2.5 0.5l2 2.5-1.2 1.3c.7 1.5 2 2.8 3.4 3.4l1.3-1.2 2.5 2-1.3 2C5 10.5 1.5 7 .5 1.8z"/></svg>
        <span>780-555-0148</span>
      </p>
      <p class="contact__line">
        <svg class="contact__icon" viewBox="0 0 12 12"><rect x="3" y="0.5" width="6" height="3"/><rect x="0.5" y="4" width="11" height="5" rx="1"/><rect x="3" y="8" width="6" height="3.5"/></svg>
        <span>780-555-0162</span>
      </p>
      <p class="contact__line">
        <svg class="contact__icon" viewBox="0 0 12 12"><path d="M0.5 2h11v8h-11z M0.5 2l5.5 4.5 5.5-4.5" stroke="#fff" stroke-width="0.8"/></svg>
        <span>office@tanridgefield.ca</span>
      </p>
    </div>
    <div class="wordmark">
      <span class="wordmark__dot"></span>
      <p class="wordmark__text">
        <span class="wordmark__name">TanRidge</span>
        <span class="wordmark__sub">Field Advisory Ltd.</span>
      </p>
    </div>
    <svg class="bottom-bands" width="580" height="90" viewBox="0 0 580 90">
      <defs>
        <linearGradient id="band-orange" x1="0" x2="1">
          <stop offset="0" stop-color="var(--accent-orange)"/>
          <stop offset="1" stop-color="var(--accent-red)"/>
        </linearGradient>
        <linearGradient id="band-blue" x1="0" y1="0" x2="0" y2="1">
          <stop offset="0" stop-color="var(--accent-blue)"/>
          <stop offset="1" stop-color="var(--accent-sky)"/>
        </linearGradient>
      </defs>
      <polygon points="0,0 230,58 0,58" fill="url(#band-orange)"/>
      <polygon points="0,58 230,58 224,66 0,66" fill="url(#band-orange)" opacity="0"/>
      <polygon points="244,44 580,44 580,90 228,90" fill="url(#band-blue)"/>
    </svg>
  </section>

</body>
</html>
```